Vantrel Ashcombe LLC

we need a business card design

Industry/Entity Type

hvac

Contact Information for Business Card

my logo

Requirements
Must have
• my logo and same colors

```html
<!DOCTYPE html>
<html lang="en">
<head>
<meta charset="utf-8">
<title>Vantrel Ashcombe LLC – Business Card</title>
<link rel="stylesheet" href="https://fonts.googleapis.com/css2?family=Arimo:wght@400;700&display=swap">
<style>
  :root {
    --stage: #3a3a3c;
    --card-blue-light: #2fa6e6;
    --card-blue-deep: #1577c4;
    --brand-navy: #1d5aa6;
    --ink-blue: #1f5fae;
    --accent-gold: #f0b23e;
    --paper: #ffffff;
    --paper-shade: #eef1f4;
  }
  * { margin: 0; padding: 0; box-sizing: border-box; }
  html, body {
    width: 1200px; height: 900px; overflow: hidden;
    background: var(--stage);
    font-family: "Arimo", Arial, sans-serif;
  }
  .canvas {
    position: relative; width: 1200px; height: 900px;
    display: flex; flex-direction: column; align-items: center;
    justify-content: center; gap: 50px;
  }
  .card {
    width: 700px; height: 400px; border-radius: 26px;
    position: relative; overflow: hidden;
  }
  .card--front {
    background: linear-gradient(135deg, var(--card-blue-light) 0%, var(--card-blue-deep) 100%);
    display: flex; align-items: center; justify-content: center;
  }
  .card--back {
    background: linear-gradient(135deg, var(--paper) 55%, var(--paper-shade) 100%);
    display: flex; align-items: center;
  }
  .brand {
    display: flex; align-items: center; gap: 16px;
  }
  .brand__dot {
    width: 34px; height: 34px; border-radius: 50%;
    flex-shrink: 0;
  }
  .brand__name {
    font-weight: 700; text-transform: uppercase;
    letter-spacing: 0.5px; line-height: 1.1;
  }
  .card--front .brand__dot { background: var(--accent-gold); }
  .card--front .brand__name { color: var(--paper); font-size: 40px; }
  .card--back .brand {
    width: 380px; padding-left: 40px;
  }
  .card--back .brand__dot { background: var(--accent-gold); width: 28px; height: 28px; }
  .card--back .brand__name { color: var(--brand-navy); font-size: 27px; }
  .divider {
    width: 3px; height: 240px; background: var(--brand-navy);
  }
  .contact {
    padding-left: 48px; color: var(--ink-blue);
  }
  .contact__name {
    font-size: 24px; font-weight: 700; text-transform: uppercase;
  }
  .contact__role {
    font-size: 13px; font-weight: 700; text-transform: uppercase;
    margin-top: 4px; margin-left: 2px;
  }
  .contact__phone {
    font-size: 26px; font-weight: 700; margin-top: 26px;
    display: flex; align-items: center; gap: 10px;
  }
  .contact__address {
    font-style: normal; font-size: 15px; font-weight: 700;
    text-transform: uppercase; margin-top: 10px; line-height: 1.4;
    margin-left: 2px;
  }
</style>
</head>
<body>
  <main class="canvas">
    <section class="card card--front" aria-label="Card front">
      <div class="brand">
        <span class="brand__dot"></span>
        <span class="brand__name">Vantrel Ashcombe LLC</span>
      </div>
    </section>

    <section class="card card--back" aria-label="Card back">
      <div class="brand">
        <span class="brand__dot"></span>
        <span class="brand__name">Vantrel Ashcombe LLC</span>
      </div>
      <div class="divider"></div>
      <div class="contact">
        <p class="contact__name">Dorian Felsworth</p>
        <p class="contact__role">Owner</p>
        <p class="contact__phone">555 0142 7788</p>
        <address class="contact__address">418 Corwell Ave N<br>Marlow Bay, FL 33891</address>
      </div>
    </section>
  </main>
</body>
</html>
```